Asian Pakistani: Wedding Invitation

Design a pakistani asian wedding invitation.
Islamic theme, with arabic text:

Text to be used:

Start with: bismillah and dua for marriage. (The Holy Quran chapter 25 verse 75 with arabic text and english translation below)

Mrs. Rukhsana Iqbal wife of (late) Mr. Nadeem Rauf Siddiqui
Cordially requests your company to grace the joyous occasion of the wedding of their beloved daughter
Sadia Siddiqui
Daughter of ( late) Mr Nadeem Rauf siddiqui
with
Imran Bashir
Son of Mr. Javed Bashir & Mrs Shaista Bashir

Insha’Allah on Thursday 29th August 2019 at Royal Orchid
12 Linden Crescent, Croydon
CR9 7TQ
Baraat Arrival 6:30

RSVP
Omar Siddiqui 07700 900412
Bilal Rehman 07700 900837
Shahzad Malik 07700 900265

Target Market(s)

Muslims

Font styles to use
Script

Colors

Designer to choose colors to be used in the design.

Requirements
Must have
• stylish calligraphy Arabic lettering of the dua requested above
• Size:
• Long 4" x 9.5"
Nice to have
• ottoman empire: Art theme

```html
<!DOCTYPE html>
<html lang="en">
<head>
<meta charset="utf-8">
<title>Wedding Invitation – Sadia &amp; Imran</title>
<link href="https://fonts.googleapis.com/css2?family=Cinzel:wght@400;700&family=Amiri:wght@400;700&family=Comfortaa:wght@500&display=swap" rel="stylesheet">
<style>
  :root {
    --page: #f2f2f2;
    --magenta: #a00c9c;
    --magenta-deep: #8a0a8a;
    --yellow: #f7ea2c;
    --gold: #d9b46c;
    --gold-soft: #c9a05a;
    --text-gold: #e8c66a;
  }
  * { margin: 0; padding: 0; box-sizing: border-box; }
  html, body { width: 1200px; height: 1200px; overflow: hidden; background: var(--page); }
  .invitation {
    position: absolute; left: 362px; top: 36px; width: 475px; height: 1128px;
    background: radial-gradient(ellipse at 50% 40%, var(--magenta) 0%, var(--magenta-deep) 100%);
    font-family: "Cinzel", serif; color: var(--text-gold);
    overflow: hidden;
  }
  .frame { position: absolute; inset: 0; }
  .block { position: absolute; left: 0; width: 100%; text-align: center; }
  .ornament { position: absolute; }
  .ornament-crown {
    left: 74px; top: 66px; width: 324px; height: 168px;
    border-radius: 162px 162px 0 0;
    background: radial-gradient(ellipse at 50% 100%, rgba(217,180,108,.55), rgba(217,180,108,.15) 70%, transparent 72%);
  }
  .ornament-rosette {
    top: 518px; width: 58px; height: 100px;
    background: radial-gradient(circle, rgba(217,180,108,.6), rgba(217,180,108,.15) 68%, transparent 70%);
  }
  .ornament-rosette.left { left: 34px; }
  .ornament-rosette.right { left: 384px; }
  .ornament-paisley {
    left: 218px; top: 810px; width: 240px; height: 306px;
    background: radial-gradient(ellipse at 60% 35%, rgba(217,180,108,.6), rgba(217,180,108,.2) 60%, transparent 75%);
  }
  .verse-arabic {
    top: 250px; font-family: "Amiri", serif; font-size: 15px; color: var(--yellow);
    direction: rtl;
  }
  .verse-english {
    top: 308px; font-size: 12px; line-height: 1.5; color: var(--text-gold);
  }
  .small { font-size: 11px; line-height: 1.45; }
  .hl { color: var(--yellow); font-weight: 700; font-size: 12.5px; }
  .host { top: 412px; }
  .request { top: 462px; }
  .name {
    font-family: "Comfortaa", sans-serif; font-weight: 500; font-size: 34px;
    color: var(--yellow); letter-spacing: 1px; text-transform: lowercase;
  }
  .bride { top: 568px; }
  .bride-parent { top: 618px; }
  .joiner { top: 668px; font-size: 10px; }
  .groom { top: 708px; }
  .groom-parents { top: 756px; }
  .details { position: absolute; left: 30px; top: 820px; width: 170px; text-align: left; }
  .insha { font-weight: 700; font-size: 14px; color: var(--yellow); }
  .date-labels { display: flex; justify-content: space-between; font-size: 11px; margin-top: 12px; width: 200px; }
  .date { font-weight: 700; font-size: 42px; color: var(--yellow); line-height: 1; width: 200px; white-space: nowrap; }
  .date sup { font-size: 24px; vertical-align: 14px; }
  .venue { margin-top: 14px; font-size: 11px; line-height: 1.5; }
  .rsvp-title { margin-top: 24px; font-weight: 700; font-size: 14px; color: var(--yellow); }
  .rsvp { margin-top: 18px; font-size: 11px; line-height: 1.5; white-space: nowrap; }
  .rsvp b { color: var(--yellow); }
</style>
</head>
<body>
<main class="invitation">
  <svg class="frame" width="475" height="1128" viewBox="0 0 475 1128" aria-hidden="true">
    <rect x="10" y="12" width="455" height="1104" fill="none" stroke="#f7ea2c" stroke-width="1.4"/>
    <path d="M47 804 V220 A190 190 0 0 1 428 220 V804" fill="none" stroke="#f7ea2c" stroke-width="2.4" stroke-dasharray="0 7" stroke-linecap="round"/>
    <path d="M55 782 V226 A183 183 0 0 1 422 226 V782 Z" fill="none" stroke="#f7ea2c" stroke-width="1.6"/>
    <line x1="10" y1="804" x2="465" y2="804" stroke="#f7ea2c" stroke-width="1.2"/>
    <line x1="62" y1="386" x2="414" y2="386" stroke="#d9b46c" stroke-width="0.8"/>
  </svg>

  <div class="ornament ornament-crown" role="img" aria-label="Gold mandala ornament in the top of the arch"></div>
  <div class="ornament ornament-rosette left" role="img" aria-label="Gold rosette ornament"></div>
  <div class="ornament ornament-rosette right" role="img" aria-label="Gold rosette ornament"></div>
  <div class="ornament ornament-paisley" role="img" aria-label="Gold floral paisley ornament"></div>

  <p class="block verse-arabic">أُولَٰئِكَ يُجْزَوْنَ الْغُرْفَةَ بِمَا صَبَرُوا وَيُلَقَّوْنَ فِيهَا تَحِيَّةً وَسَلَامًا ﴿٧٥﴾</p>
  <p class="block verse-english">They will be awarded the high place<br>forasmuch as they were steadfast, and<br>they will meet therein with welcome<br>and the ward of peace.</p>

  <p class="block small host">Mrs. <span class="hl">Rukhsana Iqbal</span> wife of (late)<br>Mr. <span class="hl">Nadeem Rauf Siddiqui</span></p>
  <p class="block small request">Cordially requests your company<br>to grace the joyous occasion<br>of the wedding of their beloved daughter</p>

  <h1 class="block name bride">Sadia Siddiqui</h1>
  <p class="block small bride-parent">Daughter of ( late) Mr <span class="hl">Nadeem Rauf siddiqui</span></p>
  <p class="block joiner">with</p>
  <h2 class="block name groom">Imran Bashir</h2>
  <p class="block small groom-parents">Son of Mr. <span class="hl">Javed Bashir</span> &amp; Mrs <span class="hl">Shaista Bashir</span></p>

  <section class="details">
    <p class="insha">Insha’Allah on</p>
    <div class="date-labels"><span>Thursday</span><span>August</span></div>
    <p class="date">29<sup>th</sup>2019</p>
    <p class="venue">at Royal Orchid<br>12 Linden Crescent, Croydon<br>CR9 7TQ<br>Baraat Arrival 6:30</p>
    <p class="rsvp-title">RSVP</p>
    <p class="rsvp">Omar Siddiqui <b>07700 900412</b><br>Bilal Rehman <b>07700 900837</b><br>Shahzad Malik <b>07700 900265</b></p>
  </section>
</main>
</body>
</html>
```